2017 New Year Membership Sale

I require a flyer to be designed for a mail box drop.

We are a 24/7 Gym and will be running a sale in January. No Joining Fee, Flexible membership options.

We are also going to have an open day on Saturday the 21st of January, everyone is welcome. Supplement samples and information. Free health measurements. Free starter PT pack if you join on the day.

We offer a 24/7 DIY gym as well as a comprehensive Personal Training Studio.

I have included the design I used last year.

Target Market(s)

Potential Members of all ages.

Industry/Entity Type

Gym

Requirements
Must have
• Our Address, Phone Number.
• Staffed Hours;
• Mon-Thur: 12pm - 7pm
• Fri-Sat: 8am - 1pm

```html
<!DOCTYPE html>
<html lang="en">
<head>
<meta charset="utf-8">
<title>Kinetix Fitness – 2017 New Year Membership Sale Flyer</title>
<link rel="stylesheet" href="https://fonts.googleapis.com/css2?family=Roboto:wght@400;700&family=Roboto+Condensed:wght@300;400;700&display=swap">
<style>
  :root {
    --orange: #f58220;
    --charcoal: #3b3b3d;
    --slate: #4b4b4e;
    --white: #ffffff;
    --ink: #2a2a2a;
    --backdrop: #2e231d;
    --photo-warm-a: #f1b25c;
    --photo-warm-b: #5a3a22;
    --photo-gym-a: #c9c9c9;
    --photo-gym-b: #6b6b6b;
    --photo-dark-a: #5a5a5a;
    --photo-dark-b: #1e1e1e;
  }
  * { box-sizing: border-box; margin: 0; padding: 0; }
  html, body { width: 1200px; height: 1200px; overflow: hidden; }
  body { background: var(--backdrop); position: relative; font-family: "Roboto", Arial, sans-serif; }

  .flyer { position: absolute; overflow: hidden; box-shadow: 0 6px 18px rgba(0,0,0,.45); }
  .abs { position: absolute; }
  .cond { font-family: "Roboto Condensed", "Arial Narrow", sans-serif; }

  /* ---------- Front: Membership Sale ---------- */
  .flyer--sale { left: 70px; top: 254px; width: 488px; height: 676px; background: var(--charcoal); }
  .sale__hero { left: 0; top: 0; width: 488px; height: 266px;
    background: radial-gradient(ellipse at 60% 35%, var(--photo-warm-a), var(--photo-warm-b) 85%); }
  .sale__brand { left: 244px; top: 266px; width: 244px; height: 73px; background: var(--orange); }
  .sale__year { left: 48px; top: 270px; color: var(--white); font-weight: 700; font-size: 62px; line-height: 1; letter-spacing: -1px; }
  .sale__newyear { left: 48px; top: 329px; color: var(--white); font-weight: 700; font-size: 35px; line-height: 1; }
  .sale__membership { left: 46px; top: 364px; color: var(--orange); font-weight: 700; font-size: 58px; line-height: 1; letter-spacing: -0.5px; }
  .sale__sale { left: 46px; top: 414px; color: var(--white); font-weight: 700; font-size: 72px; line-height: 1; letter-spacing: -1px; }
  .sale__trainer { left: 244px; top: 414px; width: 244px; height: 182px;
    background: linear-gradient(160deg, var(--photo-gym-a), var(--photo-gym-b)); }
  .sale__offers { left: 0; top: 487px; width: 238px; height: 92px; background: var(--white); padding: 2px 0 0 48px; }
  .sale__offer { color: var(--orange); font-weight: 700; font-size: 21px; line-height: 24px; }
  .sale__offer-rule { height: 1px; background: var(--orange); margin: 5px -4px 7px -48px; opacity: .8; }
  .sale__footer { left: 0; top: 596px; width: 488px; height: 80px; background: var(--orange); }

  .contact { color: var(--white); font-weight: 700; font-size: 14.5px; white-space: nowrap; }
  .contact .sep { margin: 0 6px; }
  .sale__contact { left: 48px; top: 605px; }

  .brand { display: flex; flex-direction: column; align-items: center; justify-content: center; color: var(--white);
    font-family: "Roboto Condensed", "Arial Narrow", sans-serif; font-weight: 700; }
  .brand__name { display: flex; align-items: center; gap: 8px; font-size: 24px; line-height: 1; }
  .brand__dot { width: 14px; height: 14px; border-radius: 50%; background: var(--white); }
  .brand__place { font-size: 13px; letter-spacing: 8px; margin-top: 6px; padding-left: 8px; }

  /* ---------- Back: Open Day ---------- */
  .flyer--openday { left: 614px; top: 320px; width: 484px; height: 668px; background: var(--charcoal); }
  .open__athlete { left: 0; top: 0; width: 242px; height: 384px;
    background: radial-gradient(ellipse at 50% 40%, var(--photo-dark-a), var(--photo-dark-b) 75%); }
  .open__brand { left: 46px; top: 386px; width: 194px; height: 72px; background: var(--orange); }
  .open__brand .brand__name { font-size: 21px; }
  .open__brand .brand__place { font-size: 12px; letter-spacing: 7px; }
  .open__hours { left: 46px; top: 466px; width: 196px; color: var(--white); }
  .open__hours-title { font-weight: 700; font-size: 28px; line-height: 1; letter-spacing: -0.3px; }
  .open__hours-grid { display: flex; margin-top: 6px; }
  .open__hours-col { flex: 1; font-weight: 700; font-size: 16px; line-height: 18px; }
  .open__hours-col + .open__hours-col { border-left: 1px solid var(--white); padding-left: 16px; }
  .open__hours-day { color: var(--orange); }

  .open__headline { left: 242px; top: 0; width: 242px; height: 264px; background: var(--white); padding: 42px 0 0 10px; }
  .open__line { font-family: "Roboto Condensed", "Arial Narrow", sans-serif; font-weight: 700; line-height: 1; }
  .open__line--day { color: var(--ink); font-size: 48px; }
  .open__line--sat { color: var(--ink); font-size: 33px; margin-top: 6px; }
  .open__line--date { color: var(--orange); font-size: 66px; margin-top: 4px; }
  .open__line--month { color: var(--orange); font-size: 50px; margin-top: -2px; }

  .open__details { left: 242px; top: 264px; width: 242px; height: 280px; background: var(--slate); }
  .open__welcome { left: 0; top: 10px; width: 242px; text-align: center; color: var(--white); font-weight: 300; font-size: 18px; line-height: 23px; }
  .open__free { left: 10px; top: 94px; width: 184px; height: 102px; border: 2px solid var(--white); background: var(--white); }
  .open__free-head { height: 50px; color: var(--orange); font-weight: 700; font-size: 50px; line-height: 50px; text-align: center; }
  .open__free-item { background: var(--orange); color: var(--white); font-weight: 700; font-size: 17px; height: 24px; line-height: 24px; text-align: center; }
  .open__free-item + .open__free-item { border-top: 1px solid var(--white); }
  .open__join { left: 0; top: 200px; width: 218px; text-align: center; color: var(--orange); font-weight: 700; font-size: 28px; line-height: 36px; }

  .open__offer { left: 0; top: 544px; width: 484px; height: 54px; background: var(--white); text-align: center; }
  .open__offer-title { color: var(--ink); font-weight: 700; font-size: 27px; line-height: 1; margin-top: 8px; padding-left: 40px; }
  .open__offer-sub { color: var(--ink); font-weight: 400; font-size: 11.5px; margin-top: 2px; padding-left: 40px; }
  .open__footer { left: 0; top: 598px; width: 484px; height: 70px; background: var(--orange); }
  .open__contact { left: 46px; top: 612px; }
</style>
</head>
<body>

<section class="flyer flyer--sale" aria-label="New Year membership sale flyer">
  <div class="abs sale__hero" role="img" aria-label="Photo of members training on cross-trainers in a warm-lit gym"></div>
  <div class="abs sale__brand brand">
    <div class="brand__name"><span class="brand__dot"></span>Kinetix Fitness</div>
    <div class="brand__place">HILLCREST</div>
  </div>
  <div class="abs sale__year">2017</div>
  <div class="abs sale__newyear">NEW YEAR</div>
  <div class="abs sale__membership">MEMBERSHIP</div>
  <div class="abs sale__sale">SALE</div>
  <div class="abs sale__trainer" role="img" aria-label="Photo of a personal trainer spotting a member doing dumbbell presses"></div>
  <div class="abs sale__offers cond">
    <div class="sale__offer">No Joining Fee</div>
    <div class="sale__offer-rule"></div>
    <div class="sale__offer">Flexible<br>Membership Options</div>
  </div>
  <div class="abs sale__footer"></div>
  <div class="abs contact sale__contact">Call Us Now : 3184 0526<span class="sep">|</span>www.kinetixfitness.com.au</div>
</section>

<section class="flyer flyer--openday" aria-label="Open day flyer">
  <div class="abs open__athlete" role="img" aria-label="Photo of a muscular athlete kneeling beside a dumbbell in a dark gym"></div>
  <div class="abs open__brand brand">
    <div class="brand__name"><span class="brand__dot"></span>Kinetix Fitness</div>
    <div class="brand__place">HILLCREST</div>
  </div>
  <div class="abs open__hours cond">
    <div class="open__hours-title">STAFFED HOURS</div>
    <div class="open__hours-grid">
      <div class="open__hours-col"><div class="open__hours-day">MON-THUR</div>12pm - 7pm</div>
      <div class="open__hours-col"><div class="open__hours-day">FRI-SAT</div>8am - 1pm</div>
    </div>
  </div>

  <div class="abs open__headline">
    <div class="open__line open__line--day">OPEN DAY</div>
    <div class="open__line open__line--sat">ON SATURDAY</div>
    <div class="open__line open__line--date">21st of</div>
    <div class="open__line open__line--month">JANUARY</div>
  </div>

  <div class="abs open__details cond">
    <div class="abs open__welcome">Everyone is welcome.<br>Supplement samples and<br>information.</div>
    <div class="abs open__free">
      <div class="open__free-head">FREE</div>
      <div class="open__free-item">Health Measurements.</div>
      <div class="open__free-item">Starter Pt Pack</div>
    </div>
    <div class="abs open__join">IF YOU JOIN ON<br>THE DAY.</div>
  </div>

  <div class="abs open__offer cond">
    <div class="open__offer-title">WE OFFER A 24/7 DIY GYM</div>
    <div class="open__offer-sub">as well as a comprehensive Personal Training Studio.</div>
  </div>
  <div class="abs open__footer"></div>
  <div class="abs contact open__contact">Call Us Now : 3184 0526<span class="sep">|</span>www.kinetixfitness.com.au</div>
</section>

</body>
</html>
```